Business Card Design Project

I need a new business card design for my building/development company: Kestrel Ridge Builders.

We specialise in small sub-divisions, multi-story developments and new house builds.
We handle the whole process from concept stage right throught to a fully developed property.
Updates

Target Market(s)

people looking to develop their property and need help. New property buyers

Industry/Entity Type

House

Requirements
Must have
• My logo on both sides:
Side 1: Logo taking up whole side as per old card but with a color/style change.

Side 2: Contact page: include logo but the rest just surprise me!

All contact details will be: (and need to be changable for each employee) I'll inform you of specifics before printing.

Name Surname
Position ie. Managing director
M: insert mobile
E: insert email
P.O. Box 518, Ashwell, Vic, 3094
www.kestrelridgebuilders.com.au

Nice to have
• Colors i'd like: (not necessarily all but this is the basic idea)

Black, blue, grey, silver, white

```html
<!DOCTYPE html>
<html lang="en">
<head>
<meta charset="utf-8">
<title>Kestrel Ridge Builders – Business Cards</title>
<link href="https://fonts.googleapis.com/css2?family=Source+Sans+3:wght@400;600;700&display=swap" rel="stylesheet">
<style>
  :root {
    --brand-blue: #0a8ad6;
    --brand-blue-light: #e9f6fd;
    --band-grey: #c9c9c9;
    --ink: #1b1b1b;
    --paper: #ffffff;
    --page: #ffffff;
    --edge: #2a2a2a;
  }
  * { box-sizing: border-box; margin: 0; padding: 0; }
  html, body {
    width: 1200px; height: 900px; overflow: hidden;
    background: var(--page);
    font-family: "Source Sans 3", "Myriad Pro", Arial, sans-serif;
    color: var(--ink);
  }
  .sheet { position: relative; width: 1200px; height: 900px; }

  .card {
    position: absolute;
    width: 540px; height: 310px;
    background: var(--paper);
    border: 1px solid var(--edge);
    overflow: hidden;
  }
  .card-front { left: 300px; top: 80px; }
  .card-back  { left: 380px; top: 500px; }

  .card-shapes { position: absolute; inset: 0; width: 100%; height: 100%; }

  /* Front */
  .front-brand {
    position: absolute; left: 0; right: 0; top: 118px;
    text-align: center;
  }
  .brand-name {
    font-weight: 600; font-size: 36px; letter-spacing: -0.5px;
    color: var(--ink); line-height: 1;
  }
  .brand-name .brand-mark {
    display: inline-block; width: 14px; height: 14px;
    background: var(--brand-blue); margin-right: 10px; vertical-align: 4px;
  }
  .brand-tagline {
    font-size: 15px; color: var(--ink); margin-top: 4px; letter-spacing: 0.1px;
  }
  .front-web {
    position: absolute; left: 0; right: 0; top: 226px;
    text-align: center; font-size: 15px; color: var(--ink);
  }
  .web-underline { display: block; margin: 2px auto 0; width: 230px; height: 8px; }

  /* Back */
  .back-brand { position: absolute; left: 36px; top: 110px; }
  .back-brand .brand-name { font-size: 24px; letter-spacing: -0.3px; }
  .back-brand .brand-name .brand-mark { width: 10px; height: 10px; margin-right: 7px; vertical-align: 3px; }
  .back-brand .brand-tagline { font-size: 11.5px; margin-top: 2px; }

  .person { position: absolute; left: 340px; top: 120px; }
  .person-name { font-size: 24px; font-weight: 400; line-height: 1.05; }
  .person-role { font-size: 14px; font-weight: 700; }

  .contact-list {
    position: absolute; left: 330px; top: 222px;
    list-style: none; font-size: 13px; line-height: 1.2;
  }
  .contact-list b { font-weight: 700; }
</style>
</head>
<body>
<main class="sheet">

  <section class="card card-front" aria-label="Business card front">
    <svg class="card-shapes" viewBox="0 0 540 310" preserveAspectRatio="none" aria-hidden="true">
      <polygon points="230,0 540,0 540,195" fill="var(--band-grey)"/>
      <polygon points="285,0 540,0 540,162" fill="var(--brand-blue)"/>
      <polygon points="0,118 0,310 310,310" fill="var(--band-grey)"/>
      <polygon points="0,150 0,310 255,310" fill="var(--brand-blue)"/>
    </svg>
    <div class="front-brand">
      <p class="brand-name"><span class="brand-mark"></span>Kestrel Ridge Builders</p>
      <p class="brand-tagline">renovation-construction-development</p>
    </div>
    <div class="front-web">
      <p>www.kestrelridgebuilders.com.au</p>
      <svg class="web-underline" viewBox="0 0 230 8" aria-hidden="true">
        <path d="M0 7 Q115 1 230 3 Q115 4 0 7 Z" fill="var(--brand-blue)"/>
      </svg>
    </div>
  </section>

  <section class="card card-back" aria-label="Business card back">
    <svg class="card-shapes" viewBox="0 0 540 310" preserveAspectRatio="none" aria-hidden="true">
      <defs>
        <radialGradient id="backGlow" cx="0.66" cy="0.45" r="0.6">
          <stop offset="0" stop-color="var(--brand-blue-light)"/>
          <stop offset="1" stop-color="var(--brand-blue)"/>
        </radialGradient>
      </defs>
      <rect width="540" height="310" fill="url(#backGlow)"/>
      <polygon points="250,0 295,0 385,165 190,300 150,300 340,160" fill="var(--band-grey)"/>
      <polygon points="0,0 250,0 340,160 150,310 0,162" fill="var(--paper)"/>
    </svg>
    <div class="back-brand">
      <p class="brand-name"><span class="brand-mark"></span>Kestrel Ridge Builders</p>
      <p class="brand-tagline">renovation-construction-development</p>
    </div>
    <div class="person">
      <p class="person-name">Name Surname</p>
      <p class="person-role">Position</p>
    </div>
    <ul class="contact-list">
      <li><b>T.P :</b> insert t:p number</li>
      <li><b>M :</b> insert mobile</li>
      <li><b>E :</b> insert email</li>
      <li>P.O. Box 518, Ashwell, Vic, 3094</li>
    </ul>
  </section>

</main>
</body>
</html>
```